Powerpoint template - Corporate design

We are a new company that will need a visuel design in Powerpoint based on the log and company name.

Use of primary color as attached and also the company name Hazard Beacon

Product is a safety product for use in the industry (Tag/sticker etc)

```html
<!DOCTYPE html>
<html lang="en">
<head>
<meta charset="utf-8">
<title>Hazard Beacon – Gloves</title>
<link href="https://fonts.googleapis.com/css2?family=Michroma&family=Dosis:wght@500&family=Roboto:wght@300&family=Roboto+Condensed:wght@400&display=swap" rel="stylesheet">
<style>
  :root {
    --brand-orange: #e8661e;
    --ink: #111111;
    --text-grey: #5a5a5a;
    --tagline-grey: #8a8a8a;
    --rule-grey: #6b6b6b;
    --peach: #f9cb96;
    --white: #ffffff;
    --glove-dark: #2b2b2b;
    --glove-mid: #555555;
  }
  html, body {
    margin: 0;
    padding: 0;
    overflow: hidden;
  }
  .slide {
    position: relative;
    width: 1200px;
    height: 900px;
    overflow: hidden;
    background: linear-gradient(to bottom, var(--white) 0%, var(--white) 58%, #fde9d3 75%, var(--peach) 100%);
  }
  .brand-band {
    position: absolute;
    left: 152px;
    top: 42px;
    width: 897px;
    height: 76px;
    border-radius: 38px;
    background: var(--brand-orange);
    display: flex;
    align-items: center;
    justify-content: center;
    gap: 28px;
  }
  .brand-dot {
    width: 40px;
    height: 40px;
    border-radius: 50%;
    background: var(--white);
  }
  .brand-name {
    font-family: "Michroma", sans-serif;
    font-size: 40px;
    letter-spacing: 3px;
    color: var(--ink);
    text-transform: uppercase;
    line-height: 1;
  }
  .tagline {
    position: absolute;
    left: 0;
    width: 1200px;
    top: 128px;
    text-align: center;
    font-family: "Dosis", sans-serif;
    font-weight: 500;
    font-size: 44px;
    color: var(--tagline-grey);
    margin: 0;
  }
  .header-rule {
    position: absolute;
    left: 28px;
    top: 190px;
    width: 1142px;
    height: 2px;
    background: var(--rule-grey);
  }
  .product-feature {
    position: absolute;
    left: 0;
    top: 0;
  }
  .slide-title {
    position: absolute;
    left: 700px;
    width: 424px;
    top: 310px;
    margin: 0;
    text-align: center;
    font-family: "Michroma", sans-serif;
    font-size: 46px;
    letter-spacing: 8px;
    color: var(--brand-orange);
    font-weight: 400;
  }
  .slide-body {
    position: absolute;
    left: 686px;
    top: 448px;
    font-family: "Roboto", sans-serif;
    font-weight: 300;
    font-size: 41px;
    line-height: 59px;
    color: var(--text-grey);
  }
  .slide-body p {
    margin: 0;
  }
  .slide-body .note {
    margin-top: 41px;
  }
  .site-bar {
    position: absolute;
    left: 373px;
    top: 853px;
    width: 455px;
    height: 47px;
    background: var(--brand-orange);
    color: var(--white);
    font-family: "Roboto Condensed", sans-serif;
    font-size: 33px;
    line-height: 47px;
    text-align: center;
  }
</style>
</head>
<body>
<div class="slide">
  <header>
    <div class="brand-band">
      <span class="brand-dot"></span>
      <span class="brand-name">Hazard Beacon</span>
    </div>
    <p class="tagline">Company Tagline!</p>
    <div class="header-rule"></div>
  </header>

  <svg class="product-feature" width="600" height="900" viewBox="0 0 600 900">
    <defs>
      <linearGradient id="glove-tone" x1="0" y1="0" x2="1" y2="1">
        <stop offset="0" stop-color="var(--glove-mid)"/>
        <stop offset="1" stop-color="var(--glove-dark)"/>
      </linearGradient>
    </defs>
    <rect role="img" aria-label="Photo of a pair of black insulated safety gloves"
          x="100" y="598" width="263" height="193" rx="30" fill="url(#glove-tone)"/>
    <line x1="187" y1="428" x2="199" y2="652" stroke="var(--brand-orange)" stroke-width="4"/>
    <line x1="381" y1="521" x2="252" y2="717" stroke="var(--brand-orange)" stroke-width="4"/>
    <circle cx="199" cy="652" r="7" fill="var(--brand-orange)" stroke="var(--white)" stroke-width="2"/>
    <circle cx="252" cy="717" r="7" fill="var(--brand-orange)" stroke="var(--white)" stroke-width="2"/>
    <circle role="img" aria-label="Close-up photo of the glove fingers with reflective piping"
            cx="142" cy="342" r="88" fill="url(#glove-tone)" stroke="var(--brand-orange)" stroke-width="4"/>
    <circle role="img" aria-label="Close-up photo of the elasticated glove cuff"
            cx="434" cy="457" r="88" fill="url(#glove-tone)" stroke="var(--brand-orange)" stroke-width="4"/>
  </svg>

  <h1 class="slide-title">GLOVES</h1>
  <div class="slide-body">
    <p>This is a sample template.</p>
    <p>This is a sample template.</p>
    <p class="note">A sample template.</p>
  </div>

  <footer class="site-bar">www.hazardbeacon.com</footer>
</div>
</body>
</html>
```